Dampfbadtechnik und Ausstattung Produktübersicht 2016/2017
lumavo suchte ein neues Design in der Kategorie Broschüre und hat ein Projekt auf entwurfmarkt.de gestartet.
Zielgruppe
Wir verkaufen die Technik sowie generell die Austattung für Dampfbäder. Sanitärbetriebe, Private Kunden die selbst ein Dampfbad bauen, Fliesenfachbetriebe, Wellnesscenter..
Aufgabenstellung
Alles möglich (Format, Design,..). Es handelt sich um eine Produktübersicht unserer Produkte. Unsere Kunden sind Sanitärbetriebe, Private Kunden die selbst ein Dampfbad bauen, Fliesenfachbetriebe, Wellnesscenter..
Fotos und Texte die Sie für den Folder Verwenden können finden Sie unter:
www.nebelraumwerk.com bzw. www.hitzequelle-vorta.at/de/Referenzen.html
Ich würde gerne Broschüren drucken und den Kunden zusenden.

```html
<!DOCTYPE html>
<html lang="de">
<head>
<meta charset="utf-8">
<title>Dampfgenerator „Vireo“ – Produktübersicht</title>
<link rel="stylesheet" href="https://fonts.googleapis.com/css2?family=Carlito:wght@400;700&family=Quicksand:wght@400;500&display=swap">
<style>
  :root {
    --ink: #1d1d1b;
    --title-blue: #1b4c8c;
    --accent: #00b5e6;
    --page-num: #1fa3dc;
    --paper: #ffffff;
  }
  html, body {
    margin: 0;
    padding: 0;
    overflow: hidden;
    background: var(--paper);
  }
  .spread {
    position: relative;
    width: 1200px;
    height: 423px;
    overflow: hidden;
    background: var(--paper);
    font-family: "Carlito", "Calibri", sans-serif;
    color: var(--ink);
  }
  .page-title {
    position: absolute;
    top: 53px;
    margin: 0;
    font-family: "Quicksand", sans-serif;
    font-weight: 400;
    font-size: 18px;
    letter-spacing: 0.2px;
    color: var(--title-blue);
    line-height: 1;
  }
  .page-title--left { left: 85px; }
  .page-title--right { right: 86px; }
  .header-rule {
    position: absolute;
    left: 85px;
    top: 79px;
    width: 1029px;
    height: 2px;
    background: var(--accent);
  }
  .column {
    position: absolute;
    top: 116px;
    font-size: 11.2px;
    line-height: 14.5px;
  }
  .column p { margin: 0 0 14px; }
  .column .lead { line-height: 13.3px; }
  .column strong { font-weight: 700; }
  .col-1 { left: 85px; }
  .col-2 { left: 318px; }
  .col-3 { left: 674px; }
  .col-4 { left: 905px; }
  .guarantee {
    position: absolute;
    top: 359px;
    width: 130px;
    height: 64px;
    background: var(--accent);
    color: #fff;
    font-weight: 700;
    font-size: 11.2px;
    line-height: 14.5px;
    box-sizing: border-box;
    padding: 10px 0 0 13px;
  }
  .guarantee--heating { left: 396px; }
  .guarantee--valve { left: 984px; }
  .page-number {
    position: absolute;
    top: 383px;
    font-family: "Quicksand", sans-serif;
    font-size: 11px;
    color: var(--page-num);
  }
  .page-number--left { left: 31px; }
  .page-number--right { left: 1161px; }
</style>
</head>
<body>
<main class="spread">
  <h1 class="page-title page-title--left">Dampfgenerator „Vireo“</h1>
  <h2 class="page-title page-title--right">Dampfgenerator „Vireo“</h2>
  <div class="header-rule"></div>

  <section class="column col-1">
    <p class="lead">Um die Aufheizzeit zu verkürzen ist es<br>möglich einen stärkeren Dampfgenerator<br>zu wählen.</p>
    <p><strong>Die Serviceöffnung</strong><br>Diese ermöglicht Ihnen eine einfachste,<br>sekundenschnelle Entkalkung (1/2 Zoll<br>Drehverschluss auf der Oberseite, für<br>schnelles Entkalken.</p>
    <p><strong>Komplett aus Edelstahl</strong><br>Das Innen- und Außengehäuse, Dampf-<br>austritt und Abfluss sind aus rostfreiem<br>Edelstahl – damit Sie lange Freude haben.</p>
  </section>

  <section class="column col-2">
    <p><strong>Die Hochleistungselektroden aus Edel-<br>stahl mit Antihaftüberzug</strong><br>Diese bescheren Ihnen eine extrem<br>schnelle – nach wenigen Minuten per-<br>manent saubere Bedampfung.</p>
  </section>

  <section class="column col-3">
    <p><strong>Automatische Restwasserentleerung und<br>Reinigung?</strong><br>Nach Ihrem Dampfbad entleert sich der<br>Dampfgenerator komplett von selbst.<br>Durch die automatische Frischwasser-<br>Spülung wird der Dampfgenerator sorg-<br>fältig gereinigt. Spezielle Nanoversie-<br>gelung im Inneren, sorgt für eine sehr<br>glatte Tankoberfläche, diese hilft den<br>Generator vor Kalk und Schmutz zu schüt-<br>zen. Danach schaltet er sich automatisch<br>ab.</p>
  </section>

  <section class="column col-4">
    <p>Ganz entspannt und mit einem sicheren<br>Gefühl brauchen Sie sich nach Ihrem<br>Dampfbad nur noch um eins zu kümmern:<br><strong>Um sich selbst!</strong></p>
  </section>

  <div class="guarantee guarantee--heating">5 Jahre Garantie auf<br>alle Heizelemente!</div>
  <div class="guarantee guarantee--valve">5 Jahre Garantie auf<br>das Abflussventil!</div>

  <span class="page-number page-number--left">6</span>
  <span class="page-number page-number--right">7</span>
</main>
</body>
</html>
```